Book cover for a sci fi book called The Velvet Assembly

Dear Pixel Harbor team,

I would need a book cover design for my sci fi book, 'The Velvet Assembly'.

I will start by briefing you about the book's content, then I would like to advice you about a few possible book cover scenarios that I could imagine having for the book, and on which I would like to ask you to work on.

Book abstract:

The velvet assembly is a technically developed and spiritually evolved society from a distant galaxy.

Main location the actions take place: Planet Earth, globalized world, former Northern Germany, a new isolated high tech city at the sea, called Lees, inhabitants from everywhere, one government, one religion.
• Year: 2093
• The Velvet Assembly: solar system with 7 suns. The inhabitans of the velvet assembly have no physical body, only energetical bodies. Only when visiting Earth, they can incarnate at will.

The action starts on planet Earth, where a group of 4 people, two women and two males, who meet through different circumstances and decide to follow together a spiritual and philiosophical path towards self development and evolution. They meet an incarnated master from the velvet assembly who leads their path. At the end of the books, they reach a form of enlightment and transcende to The Velvet Assembly, they only come to know at the end the truth about the real origin of their master.

For the book cover, no matter what ideas you choose, please use max three predominant colors for that, red, yellow and orange. The book cover should inspire warmth.

Suggestions for the design:
- an abstract sun
- a cosmic view of the velvet assembly
- an abstractized design of a sacred geometry shape
- sun in the upper left corner, shining with visible rays on the whole surface of the book cover, a group of 4 people with the female old master sitting by their side in the lower right corner
- an out of the box Ufo, please choose for example an asymmetrical shape, definately not the usual flying sorcer, departing from the velvet assembly solar system, cosmic view from above
- PLEASE FEEL FREE TO BRAINSTROM ON YOUR OWN IDEAS BASED ON WHAT THE BOOK ABSTRACT INSPIRED YOU

For any questions, I am atbyour disposal.

I am looking forward to your design, thank you in advance for that.

Kind regards,
Mira

Target Market(s)

Sci Fi enthusiasts
Philosophers

Font styles to use
Serif

Colors
fbee3e
ffc214
faa54b
f37122
f04a50

Requirements
Must have
• For the book cover, no matter what ideas you choose, please use max three predominant colors for that, red, yellow and orange and/or any derived hues. The book cover should inspire warmth.
• Suggestions for the design:
• - an abstract sun
• - a cosmic view of the velvet assembly
• - an abstractized design of a sacred geometry shape
• - sun in the upper left corner, shining with visible rays on the whole surface of the book cover, a group of 4 people with the female old master sitting by their side in the lower right corner
• - an out of the box Ufo, please choose for example an asymmetrical shape, definately not the usual flying sorcer, departing from the velvet assembly solar system, cosmic view from above
• - PLEASE FEEL FREE TO BRAINSTROM ON YOUR OWN IDEAS BASED ON WHAT THE BOOK ABSTRACT INSPIRED YOU
Nice to have
• Minimalistic and modern design
Should not have
• dark or grey shades
• phtographs

```html
<!DOCTYPE html>
<html lang="en">
<head>
<meta charset="utf-8">
<title>The Velvet Assembly — Book Cover</title>
<link rel="stylesheet" href="https://fonts.googleapis.com/css2?family=Cinzel:wght@500&display=swap">
<style>
  :root {
    --page-bg: #f6efe6;
    --cover-top: #f37122;
    --cover-mid: #faa54b;
    --cover-low: #f04a50;
    --sky-light: #fffbea;
    --sky-glow: #fbee3e;
    --sun-core: #ffc214;
    --sun-edge: #faa54b;
    --ring: #f37122;
    --road-top: #faa54b;
    --road-bottom: #c8502c;
    --title-ink: #5a2410;
  }
  * { margin: 0; padding: 0; box-sizing: border-box; }
  html, body {
    width: 1200px;
    height: 800px;
    overflow: hidden;
    background: var(--page-bg);
  }
  .canvas {
    position: relative;
    width: 1200px;
    height: 800px;
    display: flex;
    align-items: center;
    justify-content: center;
  }
  .book-cover {
    position: relative;
    width: 466px;
    height: 720px;
    overflow: hidden;
    background:
      radial-gradient(circle at 50% 52%, var(--cover-mid) 0%, var(--cover-top) 60%, var(--cover-low) 100%);
  }
  .cover-art {
    position: absolute;
    left: 50%;
    top: 46%;
    width: 520px;
    height: 520px;
    transform: translate(-50%, -50%);
    border-radius: 50%;
    background:
      radial-gradient(circle at 50% 68%, var(--sun-core) 0%, var(--sun-core) 22%, var(--sun-edge) 27%, rgba(250,165,75,0) 36%),
      radial-gradient(circle at 50% 62%, var(--sky-glow) 0%, rgba(251,238,62,0.45) 38%, rgba(255,251,234,0) 62%),
      radial-gradient(circle at 50% 50%, var(--sky-light) 0%, var(--sky-light) 58%, #fde1b0 78%, var(--cover-mid) 100%);
    box-shadow: 0 0 0 3px rgba(243,113,34,0.35);
  }
  .cover-art-ground {
    position: absolute;
    left: 0;
    right: 0;
    bottom: 0;
    height: 130px;
    background: linear-gradient(180deg, rgba(250,165,75,0) 0%, var(--road-top) 35%, var(--road-bottom) 100%);
  }
  .book-title {
    position: absolute;
    left: 0;
    right: 0;
    top: 196px;
    text-align: center;
    font-family: "Cinzel", serif;
    font-weight: 500;
    font-size: 32px;
    line-height: 1.05;
    letter-spacing: 1px;
    color: var(--title-ink);
    text-transform: uppercase;
  }
  .book-title span { display: block; }
</style>
</head>
<body>
  <main class="canvas">
    <section class="book-cover">
      <div class="cover-art" role="img" aria-label="Circular panorama of an inverted city skyline ringing a bright sky, with a large yellow sun rising above clouds over a road"></div>
      <div class="cover-art-ground" role="img" aria-label="Sunlit road and ground at the base of the panorama"></div>
      <h1 class="book-title"><span>The</span><span>Velvet</span><span>Assembly</span></h1>
    </section>
  </main>
</body>
</html>
```